Existing company needs Rebranding on logo and website!!

the company is called Harvest Bridge (www.harvestbridgefund.co.uk) check the site to see the existing site and logo, this has to change and must be completely different.

I want to the turn the website into a crowd funding site, but i want an inovative and interacive site. Have a look http://www.lendora.org/about/how or https://www.fundlarkly.com/ to get an idea of what is required. However i do not want my site to be anything like this. It is 2015 so web browser can do alot. when it comes to selecting project proposals on the site i want them them to pop up use your imagination your the desgner. ofcourse the site will be taking card payments and possibly bank transfers and maybe zentopay. the usual API are already on the site so you wont need to do much. the site is hosted by wordpress so i do prefer it to stay there. i am familiar with that platform.

interms of creativity you have full control we wil be working closely and i expect to be kept in the loop as things develope.

the site will also need to be turn into a mobile app which serves different purposes depending if your an investor or project sponsor.

i will give you all the information required we can communicate on chatvolt email or telephone i am flexible.

many thanks

Target Market(s)

Investors

Industry/Entity Type

Finance

Number of Pages Required

5+ page

Font styles to use
Sans Serif

Colors
3176b5
f04a50
abd036
00a990

Requirements
Must have
• i want the designer to look at my existing site www.harvestbridgefund.co.uk and come up with a better design concept.

```html
<!DOCTYPE html>
<html lang="en">
<head>
<meta charset="utf-8">
<title>Harvest Bridge</title>
<link rel="stylesheet" href="https://fonts.googleapis.com/css2?family=Open+Sans:wght@300;400;600;700&family=Open+Sans+Condensed:wght@700&display=swap">
<style>
:root{
  --green:#046a38;
  --green-dark:#032415;
  --yellow:#fcd116;
  --cream:#fdeba8;
  --ink:#222;
  --muted:#666;
  --grey-text:#888;
  --track:#dcdad2;
  --red:#ce1126;
  --white:#fff;
}
*{margin:0;padding:0;box-sizing:border-box}
html,body{width:819px;height:1200px;overflow:hidden;background:var(--white)}
body{position:relative;font-family:"Open Sans",Arial,sans-serif;color:var(--ink)}

.site-header{position:absolute;top:0;left:0;width:819px;height:57px;background:var(--white);display:flex;align-items:center}
.brand{position:absolute;left:107px;top:12px;display:flex;align-items:center;gap:8px}
.brand-dot{width:32px;height:32px;border-radius:50%;background:var(--red)}
.brand-name{font-weight:700;font-size:15px;line-height:15px;color:var(--ink);width:96px;text-transform:uppercase}
.main-nav{position:absolute;right:102px;top:21px;display:flex;gap:11px;font-size:10px}
.main-nav a{color:var(--ink);text-decoration:none}

.hero{position:absolute;top:57px;left:0;width:819px;height:320px;
  background:linear-gradient(120deg,#c9a59a 0%,#e8887a 30%,#f09a86 55%,#c88b7f 80%,#b9b0a4 100%)}
.hero-title{position:absolute;top:70px;width:100%;text-align:center;color:var(--white);font-weight:600;font-size:70px;letter-spacing:.5px}
.btn{display:inline-block;background:var(--green);color:var(--white);font-weight:700;border-radius:3px;text-align:center;text-decoration:none}
.hero .btn{position:absolute;left:293px;top:183px;width:208px;height:58px;line-height:58px;font-size:19px}
.dots{position:absolute;top:259px;left:385px;display:flex;gap:3px}
.dots span{width:6px;height:6px;border-radius:50%;background:rgba(255,255,255,.5)}
.dots span:first-child{background:var(--white)}

.project{position:absolute;top:416px;width:197px}
.project-photo{height:130px}
.photo-sea{background:linear-gradient(180deg,#b8c3c9 0%,#dfe3e4 25%,#7c8a8c 55%,#b7a58c 100%)}
.photo-flag{background:linear-gradient(180deg,#ce1126 0 33%,#fcd116 33% 66%,#006b3f 66%)}
.photo-beach{background:linear-gradient(180deg,#cfd8dc 0%,#9fb4bd 35%,#8a7e6e 60%,#d3c4a4 100%)}
.project h3{margin-top:19px;font-size:9px;font-weight:700;text-transform:uppercase}
.project .sub{font-size:7.5px;font-weight:700;margin-top:2px}
.project .author{font-size:7px;color:var(--muted);margin-top:12px}
.project .desc{font-size:8.5px;line-height:14.5px;color:var(--muted);margin-top:8px;width:175px}
.project .place{position:absolute;top:288px;left:3px;font-size:8px;color:var(--grey-text);display:flex;align-items:center;gap:3px}
.progress{position:absolute;top:305px;left:0;width:197px;height:4px;border-radius:2px;background:var(--track)}
.progress span{display:block;height:4px;border-radius:2px;background:var(--yellow)}

.cta{position:absolute;top:781px;left:0;width:819px;height:192px;background:var(--cream);text-align:center}
.cta h2{font-weight:300;font-size:28px;margin-top:16px;color:var(--ink)}
.cta p{font-size:17px;line-height:25px;color:var(--grey-text);width:500px;margin:6px auto 0}
.cta .btn{position:absolute;left:306px;top:134px;width:179px;height:36px;line-height:36px;font-size:15px}

.site-footer{position:absolute;top:973px;left:0;width:819px;height:227px;background:var(--green-dark)}
.foot-col{position:absolute;top:30px}
.foot-col h4{font-family:"Open Sans Condensed","Open Sans",sans-serif;font-weight:700;font-size:11px;color:#6f8479;text-transform:uppercase;margin-bottom:6px}
.foot-col a{display:block;color:var(--white);font-size:11px;line-height:22.5px;text-decoration:none;font-weight:600}
.foot-rule{position:absolute;top:186px;left:0;width:100%;height:1px;background:#27402f}
.copyright{position:absolute;top:193px;width:100%;text-align:center;font-size:9px;color:#9aa69e}
</style>
</head>
<body>
<header class="site-header">
  <div class="brand"><span class="brand-dot"></span><span class="brand-name">Harvest Bridge</span></div>
  <nav class="main-nav">
    <a href="#">Home</a><a href="#">About Us</a><a href="#">About Ghana</a><a href="#">Why Ghana</a><a href="#">Sponsorship</a><a href="#">News &amp; Media</a><a href="#">Contact Us</a>
  </nav>
</header>

<section class="hero" role="img" aria-label="Close-up photograph of red banknotes">
  <h1 class="hero-title">Harvest Bridge</h1>
  <a class="btn" href="#">View Project</a>
  <div class="dots"><span></span><span></span><span></span></div>
</section>

<article class="project" style="left:102px">
  <div class="project-photo photo-sea" role="img" aria-label="Photograph of children playing in the surf on a beach"></div>
  <h3>Lorem ipsum dolor:</h3>
  <p class="sub">Et purto veri nostro mei, sed dicta reprehendunt</p>
  <p class="author">Name Surname</p>
  <p class="desc">Eos fugit clita ex, cu quo putant vocibus tincidunt, nostro sanctus laboramus. Ex tincidunt disputando sea, mediocrem gloriatur te sed.</p>
  <div class="place"><svg width="9" height="11" viewBox="0 0 9 11"><path d="M4.5 0.5a4 4 0 0 1 4 4c0 3-4 6-4 6s-4-3-4-6a4 4 0 0 1 4-4z" fill="#999"/><circle cx="4.5" cy="4.5" r="1.5" fill="#fff"/></svg>City, Country</div>
  <div class="progress"><span style="width:97px"></span></div>
</article>

<article class="project" style="left:311px">
  <div class="project-photo photo-flag" role="img" aria-label="Image of the national flag of Ghana"></div>
  <h3>Lorem ipsum dolor:</h3>
  <p class="sub">Et purto veri nostro mei, sed dicta reprehendunt</p>
  <p class="author">Name Surname</p>
  <p class="desc">Eos fugit clita ex, cu quo putant vocibus tincidunt, nostro sanctus laboramus. Ex tincidunt disputando sea, mediocrem gloriatur te sed.</p>
  <div class="place"><svg width="9" height="11" viewBox="0 0 9 11"><path d="M4.5 0.5a4 4 0 0 1 4 4c0 3-4 6-4 6s-4-3-4-6a4 4 0 0 1 4-4z" fill="#999"/><circle cx="4.5" cy="4.5" r="1.5" fill="#fff"/></svg>City, Country</div>
  <div class="progress"><span style="width:52px"></span></div>
</article>

<article class="project" style="left:520px">
  <div class="project-photo photo-beach" role="img" aria-label="Photograph of a fisherman with nets on a beach"></div>
  <h3>Lorem ipsum dolor:</h3>
  <p class="sub">Et purto veri nostro mei, sed dicta reprehendunt</p>
  <p class="author">Name Surname</p>
  <p class="desc">Eos fugit clita ex, cu quo putant vocibus tincidunt, nostro sanctus laboramus. Ex tincidunt disputando sea, mediocrem gloriatur te sed.</p>
  <div class="place"><svg width="9" height="11" viewBox="0 0 9 11"><path d="M4.5 0.5a4 4 0 0 1 4 4c0 3-4 6-4 6s-4-3-4-6a4 4 0 0 1 4-4z" fill="#999"/><circle cx="4.5" cy="4.5" r="1.5" fill="#fff"/></svg>City, Country</div>
  <div class="progress"><span style="width:145px"></span></div>
</article>

<section class="cta">
  <h2>Ei nostrud adipisci scripserit</h2>
  <p>Nulla errem iudico est in, odio placerat pri ea, id eum esse sensibus. Ex vis case summo menandri.</p>
  <a class="btn" href="#">Learn more</a>
</section>

<footer class="site-footer">
  <div class="foot-col" style="left:182px"><h4>Fun Stuff</h4><a href="#">Gift Certificates</a><a href="#">Referrals</a><a href="#">Training Center</a></div>
  <div class="foot-col" style="left:311px"><h4>Support</h4><a href="#">FAQ</a><a href="#">Feedback</a><a href="#">Contact</a><a href="#">How It Works</a><a href="#">Testimonials</a></div>
  <div class="foot-col" style="left:428px"><h4>Company</h4><a href="#">About Us</a><a href="#">Partnership</a><a href="#">Blog</a></div>
  <div class="foot-col" style="left:553px"><h4>Fun Stuff</h4><a href="#">Gift Certificates</a><a href="#">Referrals</a><a href="#">Training Center</a></div>
  <div class="foot-rule"></div>
  <p class="copyright">Copyright © Harvest Bridge</p>
</footer>
</body>
</html>
```